Business Card Design needed for start up company Pramora

In need of a new business card designed for a start up company based in Sydney, Pramora is a new start up innovative Company, our mission it to make property accessible for everyday Australian and to become the leading Real Estate platform in Australia. We want it to be fresh and clean.

Industry/Entity Type

Financial

Contact Information for Business Card

Section for Name
Section for Title

PRAMORA - Where Doors Open Wide
Mobile:
Direct:

Font styles to use
Sans Serif

Colors
33a6d7
0692cd
0255a3
ffffff

Requirements
Must have
• Logo, all business card details

```html
<!DOCTYPE html>
<html lang="en">
<head>
<meta charset="utf-8">
<title>Pramora Business Card</title>
<link rel="stylesheet" href="https://fonts.googleapis.com/css2?family=Jost:ital,wght@0,400;0,500;1,400&display=swap">
<style>
  :root {
    --sky: #33a6d7;
    --ocean: #0692cd;
    --navy: #23427a;
    --white: #ffffff;
    --ink: #2b2b2b;
    --muted: #6d6d6d;
    --backdrop: #d6d6d6;
  }
  * { margin: 0; padding: 0; box-sizing: border-box; }
  html, body { width: 1200px; height: 800px; overflow: hidden; }
  body {
    background: var(--backdrop);
    font-family: "Jost", sans-serif;
    position: relative;
  }
  .card {
    position: absolute;
    top: 272px;
    width: 474px;
    height: 262px;
    background: var(--white);
    overflow: hidden;
  }
  .card--front { left: 62px; }
  .card--back { left: 642px; }

  .band { position: absolute; top: 0; bottom: 0; }
  .band--navy { background: var(--navy); }
  .band--sky { background: var(--sky); }
  .band--ocean { background: var(--ocean); }

  .card--front .band--navy { left: 0; width: 34px; }
  .card--front .band--sky { left: 42px; width: 10px; }

  .card--back .band--sky { left: 300px; width: 10px; }
  .card--back .band--navy { left: 322px; width: 76px; }
  .card--back .band--ocean { left: 410px; width: 18px; }

  .brand {
    position: absolute;
    left: 52px;
    right: 0;
    top: 0;
    bottom: 0;
    display: flex;
    align-items: center;
    justify-content: center;
  }
  .brand__name {
    font-weight: 500;
    font-size: 56px;
    letter-spacing: 6px;
    color: var(--navy);
    line-height: 1;
  }

  .holder { position: absolute; left: 36px; top: 60px; }
  .holder__name {
    font-size: 24px;
    font-weight: 400;
    letter-spacing: 0.5px;
    color: var(--ink);
    line-height: 1.05;
  }
  .holder__title {
    font-size: 14px;
    font-style: italic;
    letter-spacing: 0.8px;
    color: var(--muted);
  }
  .contact {
    position: absolute;
    left: 64px;
    top: 140px;
    display: flex;
    align-items: center;
    gap: 18px;
  }
  .contact__icon { width: 28px; height: 28px; }
  .contact__numbers {
    list-style: none;
    font-size: 17px;
    letter-spacing: 0.6px;
    color: var(--ink);
    line-height: 1.3;
  }
</style>
</head>
<body>
  <section class="card card--front" aria-label="Card front">
    <span class="band band--navy"></span>
    <span class="band band--sky"></span>
    <div class="brand">
      <span class="brand__name">PRAMORA</span>
    </div>
  </section>

  <section class="card card--back" aria-label="Card back">
    <span class="band band--sky"></span>
    <span class="band band--navy"></span>
    <span class="band band--ocean"></span>
    <div class="holder">
      <h1 class="holder__name">DANIEL HART</h1>
      <p class="holder__title">DIRECTOR</p>
    </div>
    <div class="contact">
      <svg class="contact__icon" viewBox="0 0 28 28" aria-label="Phone">
        <circle cx="14" cy="14" r="12.5" fill="none" stroke="var(--ink)" stroke-width="1.8"/>
        <path d="M10 7.5 L12 7.5 L13 10.8 L11.6 12 Q12.8 14.8 15.8 16.4 L17 15 L20.4 16 L20.4 18 Q19.5 20.2 17.2 20 Q9.5 18.8 8 10.6 Q8 8 10 7.5 Z" fill="var(--ink)"/>
      </svg>
      <ul class="contact__numbers">
        <li>123 456 789</li>
        <li>123 456 789</li>
      </ul>
    </div>
  </section>
</body>
</html>
```